Redesign Website for Tandara Flame

I have an existing website on https://www.tandaraflame-example.com.au/ and would like to have this redesigned professionally with new content (please refer to word document). We are fire protection engineers providing fire services design expertise and engineering design to a range of different clients.

We also provide drafting services to clients in the form of completing final commissioning documentation such as 'as-installed' drawings and fire services block plans to ensure compliance with the building code and relevant Australian Standards.

Target Market(s)

Builders, Architects, Consultants, Project Managers

Industry/Entity Type

Engineering Consultant

Coding

Coded - Design and coding required

Number of Pages Required

4 page

Font styles to use
Sans Serif

Requirements
Must have
• Home and about Page, fire services design page, fire block plans page, contact us page (4 Pages).

The website colour choice must match or compliment the new company logo.
Nice to have
• Quality photos of fire services installations in buildings to Australian Standards.

A website similar to this would be ideal http://corbellpyro-example.com.au
Should not have
• Stolen licensed photos

```html
<!DOCTYPE html>
<html lang="en">
<head>
<meta charset="utf-8">
<title>Tandara Flame – Fire Services and Block Plans</title>
<link rel="stylesheet" href="https://fonts.googleapis.com/css2?family=Antonio:wght@200;700&family=Poppins:wght@400;600&family=Nunito+Sans:wght@300;400&display=swap">
<style>
  :root {
    --orange: #fb8c00;
    --orange-soft: #fbb862;
    --ink: #1d1d1d;
    --body-text: #555555;
    --icon-grey: #8a8a8a;
    --blob-grey: #e4e4e4;
    --footer-grey: #9e9e9e;
    --white: #ffffff;
  }
  * { margin: 0; padding: 0; box-sizing: border-box; }
  html, body { width: 960px; height: 1200px; overflow: hidden; background: var(--white); }
  .page { position: relative; width: 960px; height: 1200px; font-family: "Nunito Sans", sans-serif; }

  .brand {
    position: absolute; left: 94px; top: 84px;
    display: flex; align-items: center; gap: 10px;
    font-family: "Poppins", sans-serif; font-weight: 600; font-size: 22px;
    color: var(--orange); letter-spacing: 0.5px; text-transform: uppercase;
  }
  .brand-mark { width: 16px; height: 16px; background: var(--orange); }

  .main-nav {
    position: absolute; top: 87px; left: 489px;
    font-family: "Poppins", sans-serif; font-size: 12.5px; color: var(--ink);
  }
  .main-nav a { position: absolute; white-space: nowrap; color: inherit; text-decoration: none; }
  .nav-home { left: 0; } .nav-about { left: 71px; } .nav-services { left: 148px; } .nav-contact { left: 230px; }
  .inquire {
    position: absolute; left: 815px; top: 83px; width: 87px; height: 33px;
    background: var(--orange); color: var(--ink); text-decoration: none;
    font-family: "Poppins", sans-serif; font-size: 12.5px;
    display: flex; align-items: center; justify-content: center;
  }

  .hero-shape { position: absolute; left: 0; top: 0; width: 960px; height: 684px; }
  .hero-art {
    position: absolute; left: 416px; top: 232px; width: 510px; height: 368px;
    border-radius: 14px;
    background: linear-gradient(160deg, #eef2f5 0%, #cfdbe6 45%, #4f86bd 70%, #9bcf8c 100%);
  }
  .hero-title {
    position: absolute; left: 56px; top: 368px; color: var(--white);
    font-family: "Antonio", sans-serif; text-transform: uppercase; line-height: 1;
  }
  .hero-title .strong { display: block; font-weight: 700; font-size: 60px; }
  .hero-title .light { display: block; font-weight: 200; font-size: 48px; margin-top: 6px; }
  .hero-text {
    position: absolute; left: 56px; top: 493px; width: 280px;
    font-size: 11px; line-height: 13.5px; color: var(--white); font-weight: 400;
  }
  .more-btn {
    position: absolute; left: 64px; top: 578px; width: 99px; height: 37px;
    background: var(--orange-soft); border-radius: 6px; color: var(--white);
    font-size: 12px; display: flex; align-items: center; justify-content: center;
  }

  .feature { position: absolute; top: 768px; text-align: center; }
  .feature svg { display: block; margin: 0 auto; width: 100px; height: 100px; }
  .feature p { margin-top: 24px; font-size: 12px; line-height: 18px; color: var(--body-text); font-weight: 300; }
  .f-speed { left: 93px; width: 190px; }
  .f-quality { left: 407px; width: 180px; }
  .f-price { left: 740px; width: 130px; }

  .site-footer {
    position: absolute; left: 0; top: 1079px; width: 960px; height: 121px;
    background: var(--footer-grey); color: var(--white); font-size: 11px;
  }
  .contact-item { position: absolute; top: 44px; display: flex; align-items: center; gap: 12px; white-space: nowrap; }
  .contact-item svg { width: 32px; height: 32px; }
  .c-phone { left: 40px; } .c-mobile { left: 250px; } .c-web { left: 452px; } .c-mail { left: 702px; }
</style>
</head>
<body>
<div class="page">

  <svg class="hero-shape" viewBox="0 0 1280 912" preserveAspectRatio="none" aria-hidden="true">
    <defs>
      <linearGradient id="heroFill" x1="0" y1="0" x2="1" y2="1">
        <stop offset="0" stop-color="#f8940f"/>
        <stop offset="0.55" stop-color="#de9a3c"/>
        <stop offset="1" stop-color="#b89c7c"/>
      </linearGradient>
    </defs>
    <path fill="url(#heroFill)" d="M0,460 C20,380 120,300 230,300 C340,300 390,410 520,415 C700,422 900,380 1050,480 C1150,560 1200,700 1150,790 C1175,830 1230,845 1280,838 L1280,912 L0,912 Z"/>
  </svg>

  <header>
    <div class="brand"><span class="brand-mark"></span>Tandara Flame</div>
    <nav class="main-nav">
      <a class="nav-home" href="#">Home</a>
      <a class="nav-about" href="#">About Us</a>
      <a class="nav-services" href="#">Services</a>
      <a class="nav-contact" href="#">Contact Us</a>
    </nav>
    <a class="inquire" href="#">Inquire</a>
  </header>

  <section class="hero">
    <h1 class="hero-title"><span class="strong">Fire Services</span><span class="light">And Block Plans</span></h1>
    <p class="hero-text">We pride ourselves in our ability to meet the demand of our clients and our ability to consistently uphold our 3 key business values in providing our services at quick turnaround, quality service at competitive pricing</p>
    <div class="more-btn">MORE</div>
    <div class="hero-art" role="img" aria-label="Illustration of two people presenting an evacuation diagram on a large laptop screen, surrounded by fire safety icons"></div>
  </section>

  <section class="features">
    <div class="feature f-speed">
      <svg viewBox="0 0 100 100" aria-hidden="true">
        <circle cx="62" cy="72" r="20" fill="var(--blob-grey)"/>
        <circle cx="40" cy="16" r="12" fill="var(--blob-grey)"/>
        <circle cx="48" cy="52" r="34" fill="#fff" stroke="var(--icon-grey)" stroke-width="1.5"/>
        <path d="M48,32 V56 H62" fill="none" stroke="var(--icon-grey)" stroke-width="1.8"/>
        <circle cx="10" cy="18" r="2.5" fill="none" stroke="var(--icon-grey)"/>
        <circle cx="86" cy="16" r="2.5" fill="none" stroke="var(--icon-grey)"/>
        <circle cx="14" cy="86" r="2.5" fill="none" stroke="var(--icon-grey)"/>
        <circle cx="80" cy="84" r="2.5" fill="none" stroke="var(--icon-grey)"/>
      </svg>
      <p>We pride ourselves on our prompt service and delivery of all of our projects. You can rely on us to meet your project deadlines!</p>
    </div>
    <div class="feature f-quality">
      <svg viewBox="0 0 100 100" aria-hidden="true">
        <circle cx="28" cy="72" r="20" fill="var(--blob-grey)"/>
        <circle cx="76" cy="30" r="14" fill="var(--blob-grey)"/>
        <path d="M16,52 A34,34 0 0 1 84,52" fill="none" stroke="var(--icon-grey)" stroke-width="2"/>
        <rect x="10" y="44" width="10" height="22" rx="4" fill="#fff" stroke="var(--icon-grey)" stroke-width="1.8"/>
        <rect x="80" y="44" width="10" height="22" rx="4" fill="#fff" stroke="var(--icon-grey)" stroke-width="1.8"/>
        <circle cx="50" cy="54" r="17" fill="#fff" stroke="var(--icon-grey)" stroke-width="1.8"/>
        <text x="50" y="62" text-anchor="middle" font-family="Nunito Sans, sans-serif" font-size="22" fill="var(--icon-grey)">?</text>
        <rect x="40" y="86" width="20" height="8" rx="4" fill="#fff" stroke="var(--icon-grey)" stroke-width="1.5"/>
        <circle cx="10" cy="20" r="2.5" fill="none" stroke="var(--icon-grey)"/>
        <circle cx="20" cy="92" r="2.5" fill="none" stroke="var(--icon-grey)"/>
      </svg>
      <p>Our customer service and our output is guaranteed to be of the highest quality. You will not be disappointed.</p>
    </div>
    <div class="feature f-price">
      <svg viewBox="0 0 100 100" aria-hidden="true">
        <circle cx="26" cy="72" r="18" fill="var(--blob-grey)"/>
        <circle cx="80" cy="78" r="16" fill="var(--blob-grey)"/>
        <circle cx="52" cy="52" r="36" fill="#fff" stroke="var(--icon-grey)" stroke-width="1.5"/>
        <g transform="rotate(-25 52 54)">
          <rect x="36" y="30" width="32" height="48" rx="5" fill="#fff" stroke="var(--icon-grey)" stroke-width="1.8"/>
          <circle cx="52" cy="38" r="3" fill="none" stroke="var(--icon-grey)" stroke-width="1.5"/>
          <text x="52" y="66" text-anchor="middle" font-family="Nunito Sans, sans-serif" font-size="18" fill="var(--icon-grey)">%</text>
        </g>
        <circle cx="12" cy="20" r="2.5" fill="none" stroke="var(--icon-grey)"/>
        <circle cx="92" cy="20" r="2.5" fill="none" stroke="var(--icon-grey)"/>
        <circle cx="14" cy="88" r="2.5" fill="none" stroke="var(--icon-grey)"/>
      </svg>
      <p>We strive to always be competitively priced are very competitively priced.</p>
    </div>
  </section>

  <footer class="site-footer">
    <div class="contact-item c-phone">
      <svg viewBox="0 0 36 36" aria-hidden="true">
        <path d="M2,14 C2,6 34,6 34,14 L34,17 L26,17 L26,13 L10,13 L10,17 L2,17 Z" fill="#fff"/>
        <path d="M9,18 L27,18 L32,30 L4,30 Z" fill="#fff"/>
        <circle cx="18" cy="24" r="4" fill="var(--footer-grey)"/>
      </svg>
      <span>67 402 918 553</span>
    </div>
    <div class="contact-item c-mobile">
      <svg viewBox="0 0 36 36" aria-hidden="true">
        <rect x="4" y="2" width="30" height="32" rx="2" fill="#fff"/>
        <path d="M2,8 H6 M2,13 H6 M2,18 H6 M2,23 H6 M2,28 H6" stroke="#fff" stroke-width="1.5"/>
        <path d="M13,10 C11,12 12,18 16,22 C20,26 26,27 28,25 L25,21 L22,23 C20,22 16,18 15,16 L17,13 Z" fill="var(--footer-grey)"/>
      </svg>
      <span>+614 00 555 123</span>
    </div>
    <div class="contact-item c-web">
      <svg viewBox="0 0 36 36" aria-hidden="true" fill="none" stroke="#c9c9c9" stroke-width="1.5">
        <circle cx="18" cy="18" r="15"/>
        <ellipse cx="18" cy="18" rx="7" ry="15"/>
        <path d="M3,18 H33 M5,10 H31 M5,26 H31 M18,3 V33"/>
      </svg>
      <span>www.tandaraflame-example.com.au</span>
    </div>
    <div class="contact-item c-mail">
      <svg viewBox="0 0 36 36" aria-hidden="true">
        <rect x="2" y="7" width="32" height="22" fill="#fff"/>
        <path d="M2,7 L18,20 L34,7 M2,29 L14,17 M34,29 L22,17" fill="none" stroke="var(--footer-grey)" stroke-width="1.5"/>
      </svg>
      <span>info@tandaraflame-example.com.au</span>
    </div>
  </footer>

</div>
</body>
</html>
```